Halden Brookworks highend custom homes

We build high end custom homes and timber frames we specialize in rustic hand made designs along with iron and concrete accents to add a modern touch 90% of my homes are buit on lake front properries attached is my logo and slogan as of now and my previous one

Target Market(s)

High end custom homes

Industry/Entity Type

Custom residential construction

Contact Information for Business Card

Been in buissness 8+ years inssured and reliable

Colors
A7469A
B969AE
D3A5CF
EDDBEB
F8F0F9

Requirements
Must have
• Must have slogan and phone number
Should not have
• A combination of rustic yet modern accents

```html
<!DOCTYPE html>
<html lang="en">
<head>
<meta charset="utf-8">
<title>Halden Brookworks – Business Card</title>
<link rel="stylesheet" href="https://fonts.googleapis.com/css2?family=Oswald:wght@600;700&family=Poppins:wght@400;500;600&display=swap">
<style>
  :root {
    --forest: #4b5a48;
    --orchid: #b262a8;
    --ink: #4a4a4a;
    --rule: #9a9a9a;
    --paper: #ffffff;
    --backdrop: #ffffff;
    --band-line: #8c9889;
  }
  * { margin: 0; padding: 0; box-sizing: border-box; }
  html, body { width: 1200px; height: 1200px; overflow: hidden; background: var(--backdrop); }
  .canvas { position: relative; width: 1200px; height: 1200px; }

  .card { position: absolute; left: 217px; width: 766px; height: 448px; overflow: hidden; }
  .card--front { top: 118px; background: var(--paper); border: 1px solid #ececec; }
  .card--back { top: 636px; background: var(--forest); }

  .abs { position: absolute; }

  /* Front: person */
  .person-name { left: 55px; top: 52px; font: 700 42px/1 "Oswald", sans-serif; color: var(--forest); letter-spacing: 1.5px; white-space: nowrap; }
  .person-role { left: 55px; top: 99px; font: 600 22px/1 "Oswald", sans-serif; color: var(--orchid); letter-spacing: 0.5px; white-space: nowrap; }
  .phone-icon { left: 54px; top: 133px; width: 26px; height: 27px; background: var(--orchid); }
  .phone-bar { left: 84px; top: 133px; height: 27px; padding: 0 8px; background: var(--orchid); color: #fff; font: 600 26px/27px "Oswald", sans-serif; letter-spacing: 0.5px; white-space: nowrap; }

  /* Front: wordmark */
  .brand { left: 410px; top: 56px; width: 320px; text-align: center; }
  .brand-square { width: 110px; height: 110px; background: var(--forest); margin: 0 auto 24px; }
  .brand-name { font: 600 22px/1 "Poppins", sans-serif; color: var(--forest); letter-spacing: 0.3px; white-space: nowrap; }
  .brand-slogan { margin-top: 12px; font: 400 15px/1 "Poppins", sans-serif; color: var(--ink); letter-spacing: 0.5px; white-space: nowrap; }

  /* Front: contact */
  .contact-row { left: 55px; display: flex; align-items: center; gap: 8px; font: 400 18px/1 "Poppins", sans-serif; color: var(--ink); white-space: nowrap; }
  .contact-row--email { top: 309px; }
  .contact-row--address { top: 336px; }
  .contact-icon { width: 19px; height: 19px; background: var(--orchid); display: flex; align-items: center; justify-content: center; }
  .contact-rule { left: 54px; top: 375px; width: 511px; height: 1px; background: var(--rule); }
  .reg-no { left: 55px; top: 390px; font: 500 17px/1 "Poppins", sans-serif; color: var(--forest); }
  .seal { left: 581px; top: 292px; }

  /* Back */
  .back-brand { left: 0; top: 118px; width: 100%; text-align: center; }
  .back-brand .brand-square { background: #fff; width: 130px; height: 130px; margin-bottom: 32px; }
  .back-brand .brand-name { color: #fff; font-size: 27px; }
  .back-brand .brand-slogan { color: #fff; font-size: 16px; margin-top: 12px; }
  .band-line { left: 0; width: 100%; height: 1px; background: var(--band-line); }
  .band-line--top { top: 378px; }
  .band-line--bottom { top: 418px; }
  .band-text { left: 0; top: 388px; width: 100%; text-align: center; color: #fff; font: 600 19px/1 "Oswald", sans-serif; letter-spacing: 0.8px; }
</style>
</head>
<body>
<div class="canvas">

  <section class="card card--front">
    <h1 class="abs person-name">OWEN HARTE</h1>
    <p class="abs person-role">MANAGING DIRECTOR</p>
    <span class="abs phone-icon">
      <svg width="26" height="27" viewBox="0 0 26 27"><path d="M8 6c1 0 2 3 2 4s-2 1-1.5 2.5 3 4 4.5 4.5 1.5-1.5 2.5-1.5 4 1 4 2-1.5 3-3 3C10 20.5 5.5 14 5.5 9 5.5 7.5 7 6 8 6z" fill="#fff"/></svg>
    </span>
    <p class="abs phone-bar">+123 555 0192</p>

    <div class="abs brand">
      <div class="brand-square"></div>
      <p class="brand-name">HALDEN BROOKWORKS</p>
      <p class="brand-slogan">• FROM SHORELINE TO SKYLINE •</p>
    </div>

    <div class="abs contact-row contact-row--email">
      <span class="contact-icon"><svg width="13" height="10" viewBox="0 0 13 10"><rect x="0.5" y="0.5" width="12" height="9" fill="none" stroke="#fff"/><path d="M0.5 0.5l6 5 6-5" fill="none" stroke="#fff"/></svg></span>
      <span>haldenbrookworks@email.com</span>
    </div>
    <div class="abs contact-row contact-row--address">
      <span class="contact-icon"><svg width="11" height="14" viewBox="0 0 11 14"><path d="M5.5 13.5S1 8.5 1 5.5a4.5 4.5 0 0 1 9 0c0 3-4.5 8-4.5 8z" fill="#fff"/><circle cx="5.5" cy="5.5" r="1.8" fill="#b262a8"/></svg></span>
      <span>118 Alder Shore Road, Suite 2, Pine Harbor</span>
    </div>
    <div class="abs contact-rule"></div>
    <p class="abs reg-no">REG NO : 7654321</p>

    <svg class="abs seal" width="134" height="134" viewBox="0 0 134 134" role="img" aria-label="Licensed and insured seal">
      <circle cx="67" cy="67" r="66" fill="var(--forest)"/>
      <circle cx="67" cy="67" r="34" fill="var(--orchid)"/>
      <path d="M52 68l10 10 20-21" fill="none" stroke="#fff" stroke-width="7" stroke-linecap="round" stroke-linejoin="round"/>
    </svg>
  </section>

  <section class="card card--back">
    <div class="abs back-brand">
      <div class="brand-square"></div>
      <p class="brand-name">HALDEN BROOKWORKS</p>
      <p class="brand-slogan">• FROM SHORELINE TO SKYLINE •</p>
    </div>
    <div class="abs band-line band-line--top"></div>
    <p class="abs band-text">HIGH END CUSTOM HOMES AND TIMBER FRAMES</p>
    <div class="abs band-line band-line--bottom"></div>
  </section>

</div>
</body>
</html>
```